Medical Professionals- Financial services

We need a logo and stationery designed for a company called Vantorel Private Capital. Based in Queensland Australia, we provide financial services and planning for medical professionals. This includes all aspects of their financial life including Debt, Wealth accumulation, Risk management and ad hoc financial services including legal and accounting.

We do not have any specific requirements for stationery itself, anything that looks quite corporate would be great.

We need stationery for the following
- Business Cards- back
- With compliments
- Letter head
- Email signature
- Display folder
Updates

Please note there must be an accredited by QBL logo on all stationery

Must also include "Vantorel Private capital Authorised Representative of QBL Asset Advisory Pty Ltd AFS Licensee no. 418593"

EXCEPTIONS for the business card

Small written, can be anywhere.

Target Market(s)

Medical Professionals- Specialist doctors, Surgeons

Industry/Entity Type

Business

Requirements
Must have
• Must incorporate a medical logo (cross or Caduceus) in a smart way. We would like to see a corporate style logo that will attract to specialist doctors and surgeons.
Nice to have
• Would like to see a corporate style logo

```html
<!DOCTYPE html>
<html lang="en">
<head>
<meta charset="utf-8">
<title>Vantorel Private Capital – Letterhead</title>
<link href="https://fonts.googleapis.com/css2?family=Montserrat:wght@400;600;700&family=Libre+Baskerville:wght@400;700&display=swap" rel="stylesheet">
<style>
  :root {
    --backdrop: #e4e5e6;
    --paper: #ffffff;
    --ink: #3a3a3a;
    --ink-soft: #6f6f6f;
    --green-dark: #216b22;
    --green-light: #7cbc3b;
    --green-brand: #3f9a2c;
    --navy: #1f2f4f;
    --signature-blue: #c9d2ea;
  }
  * { box-sizing: border-box; margin: 0; padding: 0; }
  html, body { width: 1200px; height: 968px; overflow: hidden; }
  body {
    background: var(--backdrop);
    font-family: "Montserrat", Arial, sans-serif;
    color: var(--ink);
    display: flex; align-items: center; justify-content: center;
  }
  .letterhead {
    position: relative;
    width: 640px; height: 906px;
    background: var(--paper);
    box-shadow: 0 6px 24px rgba(0,0,0,.12);
    padding: 54px 60px 0;
  }
  .letterhead__top { display: flex; justify-content: space-between; align-items: flex-start; }
  .brand { display: flex; align-items: center; gap: 10px; }
  .brand__mark { width: 34px; height: 34px; background: var(--green-brand); }
  .brand__name { font-weight: 700; font-size: 19px; letter-spacing: .5px; color: var(--green-brand); line-height: 1; }
  .contact { display: flex; gap: 14px; margin-top: 52px; font-size: 8.5px; line-height: 1.45; color: var(--ink-soft); }
  .contact__phones { border-left: 1px solid #bbb; padding-left: 12px; }
  .contact__label { color: var(--green-brand); font-weight: 700; }
  .letter { margin-top: 26px; font-size: 9.6px; line-height: 1.55; color: var(--ink); }
  .letter__salutation { font-weight: 700; font-size: 12px; margin-bottom: 8px; }
  .letter p { margin-bottom: 12px; text-align: justify; }
  .signoff { margin-top: 24px; width: 230px; margin-left: auto; text-align: right; font-size: 10px; }
  .signoff__signature { width: 150px; height: 58px; background: var(--signature-blue); border-radius: 4px; margin-bottom: 4px; }
  .signoff__name { font-weight: 700; font-size: 12.5px; margin-top: 8px; }
  .disclaimer { position: absolute; left: 60px; bottom: 58px; width: 260px; font-size: 7px; line-height: 1.4; color: var(--ink-soft); }
  .accreditation { position: absolute; right: 60px; bottom: 40px; display: flex; align-items: center; gap: 10px; font-family: "Libre Baskerville", Georgia, serif; color: var(--navy); }
  .accreditation__text { text-align: right; font-size: 10px; line-height: 1.3; }
  .accreditation__text strong { display: block; font-size: 10.5px; }
  .accreditation__badge { width: 26px; height: 26px; border-radius: 50%; background: #5a9bd6; border-left: 1px solid var(--navy); }
  .footer-band { position: absolute; left: 0; right: 0; bottom: 0; height: 22px; display: flex; }
  .footer-band__dark { width: 45%; background: var(--green-dark); height: 12px; margin-top: 10px; }
  .footer-band__light { flex: 1; background: var(--green-light); }
</style>
</head>
<body>
  <article class="letterhead">
    <header class="letterhead__top">
      <div class="brand">
        <span class="brand__mark"></span>
        <span class="brand__name">VANTOREL<br>PRIVATE CAPITAL</span>
      </div>
      <div class="contact">
        <address class="contact__address" style="font-style:normal">1042 Pelham Street<br>Kenbury, CA 94710</address>
        <div class="contact__phones">
          <span class="contact__label">Tel:</span> (510) 614-2287<br>
          <span class="contact__label">Fax:</span> (510) 614-2290
        </div>
      </div>
    </header>

    <section class="letter">
      <p class="letter__salutation">Dear sir / madame,</p>
      <p>Lorem ipsum dolor sit amet, consectetur adipisicing elit, sed do eiusmod tempor incididunt ut labore et dolore magna aliqua. Ut enim ad minim veniam, quis nostrud exercitation ullamco laboris nisi ut aliquip ex ea commodo consequat. Duis aute irure dolor in reprehenderit in voluptate velit esse cillum dolore eu fugiat nulla pariatur. Excepteur sint occaecat cupidatat non proident, sunt in culpa qui officia deserunt mollit anim id est laborum. Lorem ipsum dolor sit amet, consectetur adipisicing elit, sed do eiusmod tempor incididunt ut labore et dolore magna aliqua. Ut enim ad minim veniam, quis nostrud exercitation ullamco laboris nisi ut aliquip ex ea commodo consequat. Duis aute irure dolor in reprehenderit in voluptate velit esse cillum dolore eu fugiat nulla pariatur. Excepteur sint occaecat cupidatat non proident, sunt in culpa qui officia deserunt mollit anim id est laborum.</p>
      <p>Lorem ipsum dolor sit amet, consectetur adipisicing elit, sed do eiusmod tempor incididunt ut labore et dolore magna aliqua. Ut enim ad minim veniam, quis nostrud exercitation ullamco laboris nisi ut aliquip ex ea commodo consequat. Duis aute irure dolor in reprehenderit in voluptate velit esse cillum dolore eu fugiat nulla pariatur. Excepteur sint occaecat cupidatat non proident, sunt in culpa qui officia deserunt mollit anim id est laborum.</p>
      <p>Lorem ipsum dolor sit amet, consectetur adipisicing elit, sed do eiusmod tempor incididunt ut labore et dolore magna aliqua. Ut enim ad minim veniam, quis nostrud exercitation ullamco laboris nisi ut aliquip ex ea commodo consequat. Duis aute irure dolor in reprehenderit in voluptate velit esse cillum dolore eu fugiat nulla pariatur. Excepteur sint occaecat cupidatat non proident, sunt in culpa qui officia deserunt mollit anim id est laborum.</p>
      <p>Lorem ipsum dolor sit amet, consectetur adipisicing elit, sed do eiusmod tempor incididunt ut labore et dolore magna aliqua. Ut enim ad minim veniam, quis nostrud exercitation ullamco laboris nisi ut aliquip ex ea commodo consequat. Duis aute irure dolor in reprehenderit in voluptate velit esse cillum dolore eu fugiat nulla pariatur. Excepteur sint occaecat cupidatat non proident, sunt in culpa qui officia deserunt mollit anim id est laborum.</p>

      <div class="signoff">
        <div class="signoff__signature" role="img" aria-label="Handwritten signature of Rowan Lessing"></div>
        <div>Yours Sincerely,</div>
        <div class="signoff__name">Rowan Lessing</div>
      </div>
    </section>

    <p class="disclaimer">Vantorel Private capital Authorised Representative of QBL Asset Advisory Pty Ltd AFS Licensee no. 418593</p>

    <div class="accreditation">
      <div class="accreditation__text">Accredited by<strong>QBL Asset Advisory</strong></div>
      <span class="accreditation__badge"></span>
    </div>

    <div class="footer-band">
      <div class="footer-band__dark"></div>
      <div class="footer-band__light"></div>
    </div>
  </article>
</body>
</html>
```